Looking for business card/letterhead/email signature

Take existing logo and create full design suite of collateral

Contact Information for Business Card

Use mock details that can be edited by us

Font styles to use
Sans Serif

```html
<!DOCTYPE html>
<html lang="en">
<head>
<meta charset="utf-8">
<title>Harlow Digital Stationery Suite</title>
<link href="https://fonts.googleapis.com/css2?family=Fira+Sans:wght@400;500;700&display=swap" rel="stylesheet">
<style>
  :root {
    --backdrop: #dcdcdc;
    --paper: #f7f7f7;
    --navy: #04478a;
    --sky: #2fa3d9;
    --ink: #3a3a3a;
    --magenta: #e0245e;
    --ghost: #ececec;
  }
  * { box-sizing: border-box; margin: 0; padding: 0; }
  html, body { width: 1200px; height: 835px; overflow: hidden; }
  body {
    background: var(--backdrop);
    font-family: "Fira Sans", sans-serif;
    color: var(--ink);
    position: relative;
  }
  .sheet {
    position: absolute;
    background: var(--paper);
    box-shadow: 0 1px 2px rgba(0,0,0,0.18);
    overflow: hidden;
  }
  .wordmark {
    position: absolute;
    display: flex;
    align-items: center;
    gap: 6px;
    font-weight: 700;
    color: var(--navy);
    white-space: nowrap;
    line-height: 1;
  }
  .wordmark .dot {
    border-radius: 50%;
    background: currentColor;
    flex: none;
  }
  .wordmark.on-navy { color: #fff; }
  .ghost-mark {
    position: absolute;
    font-weight: 700;
    color: var(--ghost);
    white-space: nowrap;
    line-height: 1;
  }
  .base-band {
    position: absolute;
    left: 0; right: 0; bottom: 0;
    background: var(--navy);
  }
  .base-band .accent {
    position: absolute;
    top: 0;
    height: 4px;
    background: var(--sky);
    border-radius: 0 0 4px 4px;
  }
  .footer-line {
    position: absolute;
    font-size: 7.2px;
    white-space: nowrap;
    color: var(--ink);
  }
  .footer-line .sep { color: var(--sky); padding: 0 3px; }
  .footer-line .sep.hot { color: var(--magenta); }
  .footer-line .web { color: var(--navy); font-weight: 500; }

  /* letterhead */
  .letterhead { left: 45px; top: 74px; width: 530px; height: 686px; }
  .letterhead .wordmark { left: 40px; top: 70px; font-size: 27px; }
  .letterhead .wordmark .dot { width: 12px; height: 12px; }
  .letterhead .ghost-mark { left: 118px; top: 318px; font-size: 64px; }
  .letterhead .footer-line { left: 70px; top: 647px; }
  .letterhead .base-band { height: 12px; }
  .letterhead .base-band .accent { left: 53px; width: 424px; }

  /* envelope front */
  .envelope-front { left: 618px; top: 75px; width: 538px; height: 234px; }
  .envelope-front .wordmark { left: 33px; top: 53px; font-size: 22px; }
  .envelope-front .wordmark .dot { width: 10px; height: 10px; }
  .envelope-front .ghost-mark { left: 296px; top: 110px; font-size: 48px; }
  .envelope-front .footer-line { left: 32px; top: 202px; font-size: 6.4px; }
  .envelope-front .base-band { height: 11px; }
  .envelope-front .base-band .accent { left: 28px; width: 214px; }

  /* envelope back */
  .envelope-back { left: 618px; top: 334px; width: 538px; height: 234px; }
  .envelope-back .flap { position: absolute; left: 0; top: 0; }
  .envelope-back .wordmark { left: 50%; top: 30px; transform: translateX(-50%); font-size: 17px; }
  .envelope-back .wordmark .dot { width: 8px; height: 8px; }

  /* business cards */
  .card-front { left: 615px; top: 596px; width: 262px; height: 149px; }
  .card-front .person { position: absolute; left: 26px; top: 36px; }
  .card-front .name { font-size: 9.6px; font-weight: 700; color: var(--navy); }
  .card-front .role { font-size: 6.6px; margin-top: 1px; }
  .card-front .rule { position: absolute; left: 26px; top: 68px; width: 30px; height: 1px; background: #b5b5b5; }
  .card-front .details { position: absolute; left: 26px; top: 83px; font-size: 6.4px; line-height: 9.4px; }
  .card-front .details .gap { height: 6px; }
  .card-front .details svg { vertical-align: -1px; margin-right: 3px; }
  .card-front .wordmark { left: 165px; top: 36px; font-size: 17px; }
  .card-front .wordmark .dot { width: 8px; height: 8px; }
  .card-front .web-link { position: absolute; left: 165px; top: 118px; font-size: 6.6px; font-weight: 500; color: var(--navy); }
  .card-front .base-band { height: 11px; }
  .card-front .base-band .accent { left: 153px; width: 92px; }

  .card-back { left: 895px; top: 596px; width: 262px; height: 149px; background: var(--navy); }
  .card-back .wordmark { left: 50%; top: 50%; transform: translate(-50%, -50%); font-size: 23px; }
  .card-back .wordmark .dot { width: 10px; height: 10px; }
</style>
</head>
<body>

  <section class="sheet letterhead" aria-label="Letterhead">
    <div class="wordmark"><span class="dot"></span>Harlow Digital</div>
    <div class="ghost-mark" aria-hidden="true">Harlow</div>
    <p class="footer-line">Oakfield Park, Mill Road, Ashbury, Surrey KT30 4QX<span class="sep">|</span>000 000 0000<span class="sep hot">|</span>info@harlowdigital.com<span class="sep">|</span><span class="web">www.harlowdigital.com</span></p>
    <div class="base-band"><span class="accent"></span></div>
  </section>

  <section class="sheet envelope-front" aria-label="Envelope front">
    <div class="wordmark"><span class="dot"></span>Harlow Digital</div>
    <div class="ghost-mark" aria-hidden="true">Harlow</div>
    <p class="footer-line">Oakfield Park, Mill Road, Ashbury, Surrey KT30 4QX<span class="sep">|</span>000 000 0000</p>
    <div class="base-band"><span class="accent"></span></div>
  </section>

  <section class="sheet envelope-back" aria-label="Envelope back">
    <svg class="flap" width="538" height="80" viewBox="0 0 538 80" aria-hidden="true">
      <path d="M0 0 H538 Q532 34 510 39 L290 74 Q269 78 248 74 L28 39 Q6 34 0 0 Z" fill="var(--navy)"/>
    </svg>
    <div class="wordmark on-navy"><span class="dot"></span>Harlow Digital</div>
  </section>

  <section class="sheet card-front" aria-label="Business card front">
    <div class="person">
      <p class="name">Daniel Reeve</p>
      <p class="role">Managing Director</p>
    </div>
    <span class="rule"></span>
    <div class="details">
      <p>Oakfield Park, Mill Road</p>
      <p>Ashbury, Surrey KT30 4QX</p>
      <div class="gap"></div>
      <p><svg width="6" height="6" viewBox="0 0 10 10" aria-hidden="true"><path d="M2 1 L4 1 L4.6 3.4 L3.4 4.2 Q4.6 6 6 6.8 L6.8 5.6 L9 6.2 L9 8.4 Q8.6 9 7.6 9 Q1 8 1 2 Q1 1.2 2 1 Z" fill="var(--magenta)"/></svg>000 000 0000</p>
      <p><svg width="6" height="5" viewBox="0 0 10 8" aria-hidden="true"><rect x="0.5" y="0.5" width="9" height="7" fill="none" stroke="var(--sky)"/><path d="M0.5 0.5 L5 4.5 L9.5 0.5" fill="none" stroke="var(--sky)"/></svg>daniel@harlowdigital.com</p>
    </div>
    <div class="wordmark"><span class="dot"></span>Harlow</div>
    <p class="web-link">www.harlowdigital.com</p>
    <div class="base-band"><span class="accent"></span></div>
  </section>

  <section class="sheet card-back" aria-label="Business card back">
    <div class="wordmark on-navy"><span class="dot"></span>Harlow</div>
  </section>

</body>
</html>
```